CEO Business card - hotels and restaurant

Business card for the General Manager of 3 different businesses: 2 hotels and 1 restaurant:
Casa Ribeira Hotel
Monte Sereno - Lagos Hotel
pão com toda alegria sempre restaurant
Name and contact details:
Rui Fontoura Braga
CEO
E-mail: rui.braga@hotelcasaribeira.com
Mobile: +351 916 447 215
Please find the attached logos. You may also google it for the 3 businesses

Industry/Entity Type

Hospitality

Contact Information for Business Card

Rui Fontoura Braga
CEO

Font styles to use
Script

Colors

Designer to choose colors to be used in the design.

Requirements
Must have
• Front - Name, position and contact details
• Back - Businesses logos and info of each one
• HOTEL CASA RIBEIRA
• Address: Rua das Acácias - Nº 173 | 2440-999 BATALHA - PORTUGAL
• Phone: +351 244 551 930
• E-mail: geral@hotelcasaribeira.pt
• HOTEL MONTE SERENO - LAGOS
• Address: Avenida das Tílias, s/n | 7350-999 ELVAS - PORTUGAL
• Phone: +351 268 812 364
• E-mail: geral@hotelmsereno-lagos.pt
• "pão com toda alegria sempre" RESTAURANT
• Address: Estrada do Moinho, 42 | 2440-999 BATALHA - PORTUGAL
• Phone: +351 244 593 218
• E-mail: info@pctas.pt
Nice to have
• Something elegant and stylish but professional and very wow effect

```html
<!DOCTYPE html>
<html lang="pt">
<head>
<meta charset="utf-8">
<title>Rui Fontoura Braga – Business Card</title>
<link rel="stylesheet" href="https://fonts.googleapis.com/css2?family=Antonio:wght@400;500&family=Jost:wght@700;800&display=swap">
<style>
  :root {
    --page: #e9e6e1;
    --ink: #111111;
    --muted: #8f8f8f;
    --magenta: #e6007e;
    --icon-grey: #9a9a9a;
    --card-white: #ffffff;
    --silver-light: #f4f4f4;
    --silver-dark: #bdbdbd;
    --flower: #e8b8b0;
    --blue: #1e8fd6;
    --wine: #8a1640;
  }
  * { margin: 0; padding: 0; box-sizing: border-box; }
  html, body { width: 1200px; height: 1200px; overflow: hidden; background: var(--page); }
  .canvas { position: relative; width: 1200px; height: 1200px; }

  .card {
    position: absolute; left: 211px; width: 778px; height: 466px;
    box-shadow: 0 6px 18px rgba(0,0,0,.18);
    overflow: hidden;
  }
  .card--front { top: 90px; background: linear-gradient(100deg, var(--silver-light) 0%, #e9e9e9 50%, var(--silver-dark) 100%); }
  .card--back { top: 644px; background: var(--card-white); }

  /* front */
  .brand-mark {
    position: absolute; left: 413px; top: 22px; width: 280px; height: 280px;
    border-radius: 50%; background: var(--magenta);
    box-shadow: 4px 6px 10px rgba(0,0,0,.3);
    display: flex; align-items: center; justify-content: center;
    font-family: "Jost", sans-serif; font-weight: 800; font-size: 30px; color: #fff;
  }
  .brand-ghost {
    position: absolute; right: 14px; bottom: 18px;
    font-family: "Jost", sans-serif; font-weight: 800; font-size: 50px;
    color: rgba(255,255,255,.3); white-space: nowrap;
  }
  .front-rule {
    position: absolute; left: 0; top: 300px; width: 420px; height: 1px;
    background: linear-gradient(90deg, #777 0%, #999 70%, rgba(150,150,150,0) 100%);
  }
  .holder { position: absolute; left: 22px; top: 312px; }
  .holder__name { font-family: "Jost", sans-serif; font-weight: 800; font-size: 26px; color: var(--muted); }
  .holder__role { font-family: "Antonio", sans-serif; font-size: 17px; letter-spacing: 6px; color: var(--ink); }
  .holder__line { display: flex; align-items: center; gap: 7px; font-family: "Antonio", sans-serif; font-size: 23px; color: var(--ink); margin-top: 9px; }
  .holder__line + .holder__line { margin-top: 6px; }

  .icon { width: 28px; height: 28px; flex: none; }
  .icon--pink { fill: var(--magenta); }
  .icon--grey { fill: var(--icon-grey); }

  /* back */
  .venue { position: absolute; left: 0; width: 100%; height: 110px; }
  .venue:nth-of-type(1) { top: 48px; }
  .venue:nth-of-type(2) { top: 169px; }
  .venue:nth-of-type(3) { top: 290px; }
  .venue__mark {
    position: absolute; left: 44px; top: 6px; width: 90px;
    display: flex; flex-direction: column; align-items: center; gap: 5px;
    font-family: "Jost", sans-serif; font-weight: 700; font-size: 11px; color: var(--ink); text-align: center;
  }
  .venue__square { width: 62px; height: 62px; }
  .venue__title { position: absolute; left: 154px; top: 2px; font-family: "Jost", sans-serif; font-weight: 800; font-size: 24px; color: var(--ink); white-space: nowrap; }
  .venue__kind { position: absolute; right: 40px; top: 10px; font-family: "Jost", sans-serif; font-weight: 800; font-size: 13px; letter-spacing: 8px; margin-right: -8px; color: var(--ink); }
  .venue__line { position: absolute; left: 154px; display: flex; align-items: center; gap: 6px; font-family: "Antonio", sans-serif; font-size: 22px; color: var(--ink); white-space: nowrap; }
  .venue__line--address { top: 38px; }
  .venue__line--contact { top: 72px; }
  .venue__line .sep { margin: 0 6px; }
  .venue__line .gap { width: 4px; }
</style>
</head>
<body>
<svg width="0" height="0" style="position:absolute">
  <defs>
    <symbol id="i-mail" viewBox="0 0 28 28"><circle cx="14" cy="14" r="14"/><rect x="6.5" y="8.5" width="15" height="11" rx="1.5" fill="none" stroke="#fff" stroke-width="1.8"/><path d="M7 9.5 14 15l7-5.5" fill="none" stroke="#fff" stroke-width="1.8"/></symbol>
    <symbol id="i-phone" viewBox="0 0 28 28"><circle cx="14" cy="14" r="14"/><path d="M10 6.5c1 0 2.5 3.5 2.5 4.3 0 .9-1.5 1.2-1.5 2.3 0 1.6 2 4.7 3.6 5 .9 0 1.4-1.3 2.3-1.3.9 0 3.6 2 3.6 2.8 0 1.2-2 2.9-3.6 2.9-4.4 0-9.4-6.5-9.4-10.8 0-2.3 1.4-5.2 2.5-5.2z" fill="#fff"/></symbol>
    <symbol id="i-pin" viewBox="0 0 28 28"><circle cx="14" cy="14" r="14"/><path d="M14 5.5a6 6 0 0 0-6 6c0 4.5 6 11 6 11s6-6.5 6-11a6 6 0 0 0-6-6zm0 8.3a2.3 2.3 0 1 1 0-4.6 2.3 2.3 0 0 1 0 4.6z" fill="#fff"/></symbol>
  </defs>
</svg>

<main class="canvas">
  <section class="card card--front">
    <div class="brand-ghost">Grupo Ribeira</div>
    <div class="brand-mark">Grupo Ribeira</div>
    <div class="front-rule"></div>
    <div class="holder">
      <p class="holder__name">Rui Fontoura Braga</p>
      <p class="holder__role">CEO</p>
      <p class="holder__line"><svg class="icon icon--pink"><use href="#i-mail"/></svg>rui.braga@hotelcasaribeira.com</p>
      <p class="holder__line"><svg class="icon icon--pink"><use href="#i-phone"/></svg>+351 916 447 215</p>
    </div>
  </section>

  <section class="card card--back">
    <article class="venue">
      <div class="venue__mark"><div class="venue__square" style="background:var(--flower)"></div>Casa Ribeira</div>
      <h2 class="venue__title">Casa Ribeira</h2>
      <span class="venue__kind">HOTEL</span>
      <p class="venue__line venue__line--address"><svg class="icon icon--grey"><use href="#i-pin"/></svg>Rua das Acácias, 173<span class="sep">|</span>2440-999 BATALHA - PORTUGAL</p>
      <p class="venue__line venue__line--contact"><svg class="icon icon--grey"><use href="#i-phone"/></svg>+351 244 551 930<span class="gap"></span><svg class="icon icon--grey"><use href="#i-mail"/></svg>geral@hotelcasaribeira.pt</p>
    </article>
    <article class="venue">
      <div class="venue__mark"><div class="venue__square" style="background:var(--blue)"></div>Monte Sereno</div>
      <h2 class="venue__title">Monte Sereno - Lagos</h2>
      <span class="venue__kind">HOTEL</span>
      <p class="venue__line venue__line--address"><svg class="icon icon--grey"><use href="#i-pin"/></svg>Avenida das Tílias s/n<span class="sep">|</span>7350-999 ELVAS - PORTUGAL</p>
      <p class="venue__line venue__line--contact"><svg class="icon icon--grey"><use href="#i-phone"/></svg>+351 268 812 364<span class="gap"></span><svg class="icon icon--grey"><use href="#i-mail"/></svg>geral@hotelmsereno-lagos.pt</p>
    </article>
    <article class="venue">
      <div class="venue__mark"><div class="venue__square" style="background:var(--wine)"></div>Pão com Toda Alegria</div>
      <h2 class="venue__title">Pão com Toda Alegria Sempre</h2>
      <span class="venue__kind">RESTAURANT</span>
      <p class="venue__line venue__line--address"><svg class="icon icon--grey"><use href="#i-pin"/></svg>Estrada do Moinho, 42<span class="sep">|</span>2440-999 BATALHA - PORTUGAL</p>
      <p class="venue__line venue__line--contact"><svg class="icon icon--grey"><use href="#i-phone"/></svg>+351 244 593 218<span class="gap"></span><svg class="icon icon--grey"><use href="#i-mail"/></svg>info@pctas.pt</p>
    </article>
  </section>
</main>
</body>
</html>
```